Sponsorship Brochure for Farmers Market

We are looking for a sponsorship brochure for our children's farmers market. This brochure will be sent to companies to request donations of money to help fund the farmer's market so kids can attend for free.

Brochure can be either letter or legal size.
You can do one-sided or two-sided.
You can do a one page brochure or tri-fold.
Option but not required: You can adjust colors on the logos to match your design
Each Sponorship Item should stand out as it's own independant section with Photos / Price / Title
Feel Free to Find Your Own additional Stock Art or Images, we provided some just for examples but you are open to using whatever works best for your design.

TEXT: Please feel free to rearrange text placement as needed for your design.

--SPONSOR THE CHILDREN’S FARMER’S MARKET!

DONATE - VOLUNTEER – BUILD

Contact: ________________________ Email: ___________ Phone: _________

You can help in several ways….donate funds, volunteer or help build the structures

Families, kids and the local community get to experience this one of a kind weekly farmer’s market where children and beginning farmers sell produce, flowers and the products they make from forest and farm materials.

Children learn farming, hard work, marketing and commerce. Kids can participate for one Saturday or the entire season.
__________________________________________________________________
Sponsor a Children’s Booth for Saturday Farmer’s Market:

$50 for One Saturday / $200 for Entire Month / $600 Entire Market Season

___________________________________________________________________
(Photo) $2,500 or Volunteer to Build Children’s Lemonade Stand

____________________________________________________________________
(Photos) $350 or Volunteer to Build Picnic Tables

(Photos) $3,500-$5000 or Volunteer to Build Children’s Farm Stands / Peddler Wagons

(Photo) $20,0000 Market, Picnic and Educational Pavilion
______________________________________________________________________

(Photo) $15,000 Baby Chick Nursery and Coop
________________________________________________________________________
(Photo) $20,000 Children’s Farm Playground
_________________________________________________________________________

```html
<!DOCTYPE html>
<html lang="en">
<head>
<meta charset="utf-8">
<title>Sponsor the Children's Farmer's Market</title>
<link rel="stylesheet" href="https://fonts.googleapis.com/css2?family=Fredoka:wght@500;600;700&family=Arimo:ital,wght@0,400;0,700;1,700&display=swap">
<style>
:root{
  --green:#3aa935;
  --green-dark:#1d8a3a;
  --green-deep:#157a32;
  --lime:#8cc63f;
  --lime-light:#c8e66a;
  --orange:#f7941d;
  --yellow:#fff35c;
  --ink:#222;
  --white:#fff;
}
*{box-sizing:border-box;margin:0;padding:0}
html,body{width:1200px;height:900px;overflow:hidden;background:var(--white)}
body{position:relative;font-family:'Arimo',Arial,sans-serif;color:var(--ink)}
.page{position:absolute;top:93px;width:506px;height:717px;overflow:hidden;box-shadow:0 1px 4px rgba(0,0,0,.25)}
.page--front{left:62px;background:var(--white)}
.page--back{left:617px;background:var(--green-deep)}
.abs{position:absolute}
.photo{position:absolute;overflow:hidden}
.photo--circle{border-radius:50%;border:5px solid var(--lime)}
.art{position:absolute;border-radius:40% 40% 20% 20%}

/* front */
.front__field{left:0;top:0;width:506px;height:560px;background:linear-gradient(180deg,#5ec43a 0%,#3aa935 55%,#2f9a33 100%)}
.sign{left:57px;top:24px;width:392px;height:150px}
.sign__kicker{left:57px;top:38px;width:392px;text-align:center;font-family:'Fredoka',sans-serif;font-weight:700;font-size:30px;color:var(--green-dark);letter-spacing:.5px}
.sign__title{left:57px;top:80px;width:392px;text-align:center;font-family:'Fredoka',sans-serif;font-weight:700;font-size:34px;line-height:38px;color:var(--white);text-shadow:0 2px 0 var(--green-dark)}
.front__ground{left:-20px;top:520px;width:546px;height:120px;background:var(--white);border-radius:50% 50% 0 0 / 40% 40% 0 0}
.actions{left:0;top:583px;width:506px;display:flex;justify-content:center;gap:16px;font-family:'Fredoka',sans-serif;font-weight:700;font-size:27px;color:var(--green)}
.actions span{display:flex;align-items:center;gap:6px}
.contact{font-size:11px;font-weight:700;color:var(--ink);white-space:nowrap}
.front__contact{left:26px;top:636px}
.help-band{left:0;top:667px;width:506px;height:50px;background:var(--lime);text-align:center;padding-top:7px}
.help-band__lead{font-size:13px;color:var(--white)}
.help-band__ways{font-size:12.5px;font-weight:700;color:var(--green-deep);margin-top:3px}

/* back */
.back__top{left:0;top:0;width:506px;height:273px;background:linear-gradient(160deg,#b8dc4a 0%,#8cc63f 100%)}
.back__curve{left:150px;top:60px;width:420px;height:260px;background:var(--lime);border-radius:50% 0 0 50% / 50% 0 0 50%}
.intro{left:250px;top:112px;width:245px;font-size:10px;line-height:13px;color:var(--white)}
.intro__note{margin-top:8px;font-size:11px;line-height:14px;font-weight:700;font-style:italic;color:var(--green-deep)}
.booth-band{left:0;top:273px;width:506px;height:36px;background:var(--orange);padding:4px 0 0 38px}
.booth-band__title{font-size:10.5px;font-weight:700;color:var(--white);text-transform:uppercase}
.booth-band__prices{font-size:12px;font-weight:700;color:var(--yellow);margin-top:2px}
.tiers{left:16px;top:318px;width:474px;display:grid;grid-template-columns:1fr 1fr;column-gap:10px;row-gap:9px}
.tier{height:107px;border:2px dashed rgba(255,255,255,.75);background:var(--green);display:flex;align-items:center;padding:6px;gap:10px}
.tier__photo{position:relative;width:80px;height:92px;flex:none}
.tier__photo--wide{width:112px}
.tier__text{color:var(--white);font-size:11px;line-height:13px;font-weight:700}
.tier__price{display:block;font-size:19px;line-height:22px;font-weight:400}
.back__contact-box{left:18px;top:657px;width:470px;height:42px;background:var(--white);padding:14px 0 0 14px}
</style>
</head>
<body>

<section class="page page--front" aria-label="Front: sponsor the children's farmer's market">
  <div class="abs front__field"></div>

  <svg class="abs sign" viewBox="0 0 392 150" aria-hidden="true">
    <path d="M20 48 H85 V20 Q85 4 101 4 H291 Q307 4 307 20 V48 H372 Q384 48 384 60 V134 Q384 146 372 146 H20 Q8 146 8 134 V60 Q8 48 20 48 Z" fill="#c8e66a" stroke="#f7941d" stroke-width="5"/>
    <path d="M30 56 H362 V138 H30 Z" fill="#7cc242" opacity=".55"/>
  </svg>
  <div class="abs sign__kicker">SPONSOR</div>
  <div class="abs sign__title">THE CHILDREN'S<br>FARMER'S MARKET!</div>

  <div class="art" role="img" aria-label="Cartoon farmer girl carrying a basket of vegetables" style="left:20px;top:200px;width:92px;height:105px;background:linear-gradient(180deg,#e89a3c,#3b6fb6)"></div>

  <div class="photo photo--circle" role="img" aria-label="Photo of a girl holding a crate of strawberries in a field" style="left:-43px;top:333px;width:240px;height:240px;background:linear-gradient(160deg,#7fb24a,#4e7a30 60%,#8a6a3c)"></div>
  <div class="photo photo--circle" role="img" aria-label="Photo of two girls carrying baskets of vegetables" style="left:338px;top:347px;width:186px;height:186px;background:linear-gradient(160deg,#9cc86a,#4d8f3a 55%,#c65a4a)"></div>
  <div class="photo photo--circle" role="img" aria-label="Photo of a smiling girl holding a crate of strawberries" style="left:167px;top:207px;width:200px;height:200px;background:linear-gradient(170deg,#cfe2b8,#8db86a 45%,#d8544a 80%)"></div>

  <div class="abs front__ground"></div>
  <div class="art" role="img" aria-label="Cartoon farmer boy and girl with a crate of produce" style="left:190px;top:480px;width:120px;height:95px;background:linear-gradient(180deg,#c98a4c,#3b6fb6 60%,#b5432e)"></div>

  <div class="abs actions">
    <span><svg width="20" height="20" viewBox="0 0 20 20" aria-hidden="true"><path d="M2 11 L8 17 L18 4" fill="none" stroke="#8cc63f" stroke-width="4" stroke-linecap="round" stroke-linejoin="round"/></svg>DONATE</span>
    <span><svg width="20" height="20" viewBox="0 0 20 20" aria-hidden="true"><path d="M2 11 L8 17 L18 4" fill="none" stroke="#8cc63f" stroke-width="4" stroke-linecap="round" stroke-linejoin="round"/></svg>VOLUNTEER</span>
    <span><svg width="20" height="20" viewBox="0 0 20 20" aria-hidden="true"><path d="M2 11 L8 17 L18 4" fill="none" stroke="#8cc63f" stroke-width="4" stroke-linecap="round" stroke-linejoin="round"/></svg>BUILD</span>
  </div>
  <p class="abs contact front__contact">Contact: ______________________________ Email: __________________ Phone: _______________</p>

  <div class="abs help-band">
    <p class="help-band__lead">You can help in several ways….</p>
    <p class="help-band__ways">DONATE FUNDS, VOLUNTEER OR HELP BUILD THE STRUCTURES</p>
  </div>
</section>

<section class="page page--back" aria-label="Back: sponsorship options">
  <div class="abs back__top"></div>
  <div class="abs back__curve"></div>

  <div class="photo photo--circle" role="img" aria-label="Photo of a girl in a straw hat with a crate of fresh vegetables at a market" style="left:-40px;top:-70px;width:290px;height:290px;background:linear-gradient(170deg,#e0a64a,#c7d6b0 45%,#6f9a50 75%)"></div>
  <div class="photo photo--circle" role="img" aria-label="Photo of a decorated farm wagon at the market" style="left:222px;top:-55px;width:150px;height:150px;background:linear-gradient(170deg,#a8c8e8,#6a7a8a 55%,#4f6e3a)"></div>
  <div class="photo photo--circle" role="img" aria-label="Photo of two children holding a chicken" style="left:365px;top:-50px;width:160px;height:150px;background:linear-gradient(170deg,#d9d2c8,#a06f4a 55%,#e9e2da)"></div>

  <div class="art" role="img" aria-label="Cartoon farmer girl in overalls" style="left:4px;top:138px;width:78px;height:168px;background:linear-gradient(180deg,#7a3a20,#f0c89a 30%,#3b6fb6 65%,#f2c12e)"></div>

  <div class="abs intro">
    <p>Families, kids and the local community get to experience this one of a kind weekly farmer's market where children and beginning farmers sell produce, flowers and the products they make from forest and farm materials.</p>
    <p class="intro__note">Children learn farming, hard work, marketing and commerce. Kids can participate for one Saturday or the entire season.</p>
  </div>

  <div class="abs booth-band">
    <p class="booth-band__title">Sponsor a children's booth for Saturday farmer's market:</p>
    <p class="booth-band__prices">$50 for One Saturday / $200 for Entire Month / $600 Entire Market</p>
  </div>
  <div class="art" role="img" aria-label="Cartoon farmer boy with a watering can" style="left:462px;top:230px;width:44px;height:80px;background:linear-gradient(180deg,#8a5a30,#f0c89a 30%,#3b6fb6 60%,#f2c12e)"></div>

  <div class="abs tiers">
    <article class="tier">
      <div class="photo tier__photo tier__photo--wide" role="img" aria-label="Photo of a children's lemonade stand" style="background:linear-gradient(170deg,#8fb86a,#e0c060 55%,#6a8a40)"></div>
      <p class="tier__text"><span class="tier__price">$2,500</span>or Volunteer to Build Children's Lemonade Stand</p>
    </article>
    <article class="tier">
      <div class="photo tier__photo tier__photo--wide" role="img" aria-label="Photo of wooden picnic tables" style="background:linear-gradient(170deg,#5e8a4a,#a05a30 60%,#7a9a5a)"></div>
      <p class="tier__text"><span class="tier__price">$350</span>or Volunteer to Build Picnic Tables</p>
    </article>
    <article class="tier">
      <div class="photo tier__photo tier__photo--wide" role="img" aria-label="Photo of children at a farm stand with produce" style="background:linear-gradient(170deg,#e07a3a,#7a3a2a 50%,#6a9a4a)"></div>
      <p class="tier__text"><span class="tier__price">$3,500 -$5000</span>or Volunteer to Build Children's Farm Stands / Peddler Wagons</p>
    </article>
    <article class="tier">
      <div class="photo tier__photo tier__photo--wide" role="img" aria-label="Photo of a picnic area on a lawn" style="background:linear-gradient(170deg,#2e5a2a,#5a8a3a 55%,#7ab04a)"></div>
      <p class="tier__text"><span class="tier__price">$20,0000</span>Market, Picnic and Educational Pavilion</p>
    </article>
    <article class="tier">
      <div class="photo tier__photo tier__photo--wide" role="img" aria-label="Photo of a small red chicken coop" style="background:linear-gradient(170deg,#c8d8e8,#a84a4a 50%,#5a7a3a)"></div>
      <p class="tier__text"><span class="tier__price">$15,000</span>Baby Chick Nursery and Coop</p>
    </article>
    <article class="tier">
      <div class="photo tier__photo tier__photo--wide" role="img" aria-label="Photo of a farm playground with a tractor" style="background:linear-gradient(170deg,#9ac0e8,#c84a3a 45%,#6a8a3a)"></div>
      <p class="tier__text"><span class="tier__price">$20,000</span>Children's Farm Playground</p>
    </article>
  </div>

  <div class="abs back__contact-box">
    <p class="contact" style="font-weight:400">Contact: ___________________________ Email: ____________ Phone: __________</p>
  </div>
</section>

</body>
</html>
```